Quill Harbor Gems Website revamp

Hi,

We need a working WordPress theme, not just a .PSD file. Thank you.

We need a complete revamp of our website. We sell lab grown diamonds online. We sell the idea that everyone should be able to afford a diamond. Thus our diamonds are priced very reasonably. Our selling point "the joy of giving and receiving a diamond in a little box".

Our range of products includes rings, bangles, necklace, ear rings etc. We currently only operate in Singapore. Some photos of our products are on our websites.

Need.
- Clean look and feel, simplistic preferably white and soft colours
- Easy to navigate
- No banners
- E Com
- Introduction page
- Willing to change logo if needed

Existing page: www.quillharborgems-example.com

Target Market(s)

Young ladies
Ladies
Men buying for ladies
Young boyfriends fresh out of school buying for love ones
Working ladies to match what they wear to work

Industry/Entity Type

Online

Requirements
Must have
• ECOM. Product shopping cart
Pictures uploads
Intro page
Nice to have
• Pastel colors preferred. - Color scheme is important in our business to create a long term impression. Color scheme will also be used for next potential project, i.e. packaging design.

Should not have
• Should not have old style fonts.

```html
<!DOCTYPE html>
<html lang="en">
<head>
<meta charset="utf-8">
<title>Quill Harbor Gems – Our Diamonds</title>
<link href="https://fonts.googleapis.com/css2?family=Arimo:wght@400;700&family=PT+Sans:wght@400;700&family=Open+Sans:wght@400&display=swap" rel="stylesheet">
<style>
  :root{
    --ink:#222;
    --text:#444;
    --muted:#777;
    --topbar:#333;
    --rule:#d9dde6;
    --rule-blue:#c9d6ea;
    --footer-bg:#f4f4f4;
    --search-blue:#6b93c6;
    --cart-orange:#f0674b;
    --gift-teal:#5fcfc4;
    --white:#fff;
  }
  *{box-sizing:border-box;margin:0;padding:0}
  html,body{width:993px;height:1200px;overflow:hidden;background:var(--white)}
  body{position:relative;font-family:"Arimo",Arial,sans-serif;color:var(--text)}
  a{color:inherit;text-decoration:none}
  .abs{position:absolute}

  /* top bar */
  .top-bar{left:0;top:0;width:993px;height:30px;background:var(--topbar)}
  .top-bar__links{right:20px;top:9px;font-size:11px;color:var(--white);display:flex;gap:22px}

  /* header */
  .brand{left:49px;top:90px;display:flex;align-items:center;gap:10px}
  .brand__mark{width:18px;height:18px;background:#5a4a3a}
  .brand__name{font-family:"PT Sans",sans-serif;font-size:22px;font-weight:400;color:#5a4a3a}
  .welcome{left:258px;top:68px;font-size:12px;color:var(--ink)}
  .welcome a{text-decoration:underline}
  .search{left:664px;top:55px;width:160px;height:34px;border-radius:17px;background:var(--white);border:1px solid #eee;padding:9px 14px;font-size:12px;color:#999}
  .search__btn{left:819px;top:53px;width:37px;height:37px;border-radius:50%;background:var(--search-blue)}
  .cart__btn{left:866px;top:53px;width:37px;height:37px;border-radius:50%;background:var(--cart-orange)}
  .cart__label{left:910px;top:65px;font-size:12px;font-weight:700;color:var(--ink)}
  .header-rule{left:258px;top:118px;width:715px;height:1px;background:var(--rule)}
  .main-nav{left:258px;top:134px;display:flex;gap:0;font-size:15px;font-weight:700;color:var(--ink)}
  .main-nav a{position:absolute;white-space:nowrap}

  /* content */
  .breadcrumb{left:20px;top:194px;font-size:13px;color:var(--muted)}
  .breadcrumb small{font-size:11px}
  .page-title{left:20px;top:284px;font-family:"Open Sans",sans-serif;font-weight:400;font-size:29px;color:var(--ink);letter-spacing:.5px}
  .title-rule{left:20px;top:338px;width:953px;height:2px;border-top:1px solid var(--rule-blue);border-bottom:1px solid #eef2f8}
  .product-visual{left:49px;top:384px;width:168px;height:188px;border-radius:6px;background:linear-gradient(160deg,#a8ece4,var(--gift-teal) 60%,#3fb3a8)}
  .side-rule{left:20px;top:609px;width:232px;height:1px;background:var(--rule-blue)}
  .intro{left:270px;top:382px;width:600px;font-size:12px;line-height:14px;color:var(--ink)}
  .intro p{margin-bottom:14px}

  /* footer */
  .site-footer{left:0;top:867px;width:993px;height:226px;background:var(--footer-bg)}
  .footer-col{top:926px;width:225px}
  .footer-col h3{font-family:"PT Sans",sans-serif;font-weight:400;font-size:18px;color:var(--ink);letter-spacing:.5px;padding-bottom:10px;border-bottom:1px solid var(--rule)}
  .footer-col ul{list-style:none;margin-top:18px;font-family:"PT Sans",sans-serif;font-size:12px;color:var(--text)}
  .footer-col li{height:23px}
  .contact-item{display:flex;gap:10px;font-family:"PT Sans",sans-serif;font-size:12px;line-height:14px;color:var(--text);margin-bottom:8px}
  .contact-item svg{flex:none;margin-top:1px}

  /* bottom bar */
  .newsletter__icon{left:20px;top:1122px;width:34px;height:34px;border-radius:50%;background:var(--cart-orange)}
  .newsletter__title{left:65px;top:1128px;font-family:"PT Sans",sans-serif;font-size:17px;color:var(--ink)}
  .newsletter__note{left:171px;top:1133px;font-family:"PT Sans",sans-serif;font-size:11px;color:var(--text)}
  .newsletter__field{left:483px;top:1117px;width:218px;height:44px;border:1px solid #ccc;border-radius:22px;padding:14px 18px;font-family:"PT Sans",sans-serif;font-size:12px;color:var(--muted)}
  .bottom-divider{left:729px;top:1100px;width:1px;height:100px;background:#eee}
  .payments{left:753px;top:1123px;display:flex;gap:8px}
  .payments span{width:49px;height:32px;border-radius:3px;border:1px solid #ddd}
</style>
</head>
<body>
  <div class="abs top-bar"></div>
  <nav class="abs top-bar__links"><a href="#">My Account</a><a href="#">Contact Us</a></nav>

  <header>
    <a class="abs brand" href="#"><span class="brand__mark"></span><span class="brand__name">Quill Harbor Gems</span></a>
    <p class="abs welcome">Welcome visitor you can <a href="#">login</a> or <a href="#">create an account</a>.</p>
    <div class="abs search">Search</div>
    <div class="abs search__btn">
      <svg width="37" height="37" viewBox="0 0 37 37"><circle cx="17" cy="17" r="5.5" fill="none" stroke="#fff" stroke-width="2"/><line x1="21" y1="21" x2="25" y2="25" stroke="#fff" stroke-width="2"/></svg>
    </div>
    <div class="abs cart__btn">
      <svg width="37" height="37" viewBox="0 0 37 37"><path d="M11 14h15l-2 9H13z" fill="#fff"/><circle cx="15" cy="26" r="1.5" fill="#fff"/><circle cx="22" cy="26" r="1.5" fill="#fff"/></svg>
    </div>
    <span class="abs cart__label">CART £0</span>
    <div class="abs header-rule"></div>
    <nav class="abs main-nav">
      <a href="#" style="left:0">HOME</a>
      <a href="#" style="left:71px">OUR STORY</a>
      <a href="#" style="left:181px">OUR DIAMONDS</a>
      <a href="#" style="left:319px">SHOP</a>
      <a href="#" style="left:388px">CONTACT US</a>
    </nav>
  </header>

  <main>
    <p class="abs breadcrumb"><small>Home</small> / OUR DIAMONDS</p>
    <h1 class="abs page-title">OUR DIAMONDS</h1>
    <div class="abs title-rule"></div>
    <div class="abs product-visual" role="img" aria-label="Teal gift box tied with a white ribbon bow"></div>
    <div class="abs side-rule"></div>
    <div class="abs intro">
      <p>We will be launching Quill Harbor Gems soon, do stay tuned for our official launching of our website and sales promotion.<br>In the meantime do check out how our diamonds are created in Our Diamond page.</p>
      <p>You may also want to take a look at our sample products.</p>
    </div>
  </main>

  <footer>
    <div class="abs site-footer"></div>

    <section class="abs footer-col" style="left:20px">
      <h3>CONTACT US</h3>
      <div style="margin-top:20px">
        <div class="contact-item">
          <svg width="12" height="14" viewBox="0 0 12 14"><path d="M6 0a5 5 0 0 0-5 5c0 4 5 9 5 9s5-5 5-9a5 5 0 0 0-5-5z" fill="#5b7fb5"/><circle cx="6" cy="5" r="1.8" fill="#f4f4f4"/></svg>
          <span>27 Lantern Quay Road,<br>#03-12 Harbor Light Mall,<br>Singapore 400123</span>
        </div>
        <div class="contact-item">
          <svg width="14" height="12" viewBox="0 0 14 12"><path d="M1 3c0-2 12-2 12 0v2h-3V3.5H4V5H1z" fill="#5b7fb5"/><rect x="3" y="6" width="8" height="5" rx="1" fill="#5b7fb5"/></svg>
          <span>+65 9000 1234</span>
        </div>
        <div class="contact-item">
          <svg width="14" height="11" viewBox="0 0 14 11"><rect x=".5" y=".5" width="13" height="10" rx="1" fill="none" stroke="#5b7fb5"/><path d="M1 1l6 5 6-5" fill="none" stroke="#5b7fb5"/></svg>
          <span>info@quillharborgems-example.com</span>
        </div>
      </div>
    </section>

    <section class="abs footer-col" style="left:264px">
      <h3>INFORMATION</h3>
      <ul><li>Sample Page</li><li>Contact Us</li><li>News</li></ul>
    </section>

    <section class="abs footer-col" style="left:508px">
      <h3>CUSTOMER SERVICE</h3>
      <ul><li>Checkout</li><li>Cart</li><li>Privacy Policy</li></ul>
    </section>

    <section class="abs footer-col" style="left:753px;width:220px">
      <h3>MY ACCOUNT</h3>
      <ul><li>My Account</li><li>Edit My Address</li><li>Logout</li><li>Lost Password</li></ul>
    </section>

    <div class="abs newsletter__icon">
      <svg width="34" height="34" viewBox="0 0 34 34"><rect x="10" y="12" width="14" height="10" rx="1" fill="#fff"/><path d="M10 12l7 6 7-6" fill="none" stroke="#f0674b" stroke-width="1.2"/></svg>
    </div>
    <span class="abs newsletter__title">Newsletter</span>
    <span class="abs newsletter__note">Subscribe to notifications about discounts from our store</span>
    <div class="abs newsletter__field">Email
      <svg style="position:absolute;right:16px;top:14px" width="10" height="16" viewBox="0 0 10 16"><path d="M2 1l6 7-6 7" fill="none" stroke="#555" stroke-width="1.6"/></svg>
    </div>
    <div class="abs bottom-divider"></div>
    <div class="abs payments" aria-label="Accepted payment methods">
      <span style="background:#e9eef8"></span>
      <span style="background:#fdf4dc"></span>
      <span style="background:#2b2b2b"></span>
      <span style="background:#3a3a3a"></span>
    </div>
  </footer>
</body>
</html>
```